Attic Rivers (Progressive House Album)

Hey Guys,

I'm a music artist and I need a CD Cover done for my new album.The album is called "Attic Rivers" and I really need something artistic, almost like a painting that reflects the name of the album.

Also please feel free to step out from the whole "almost like a painting" box, if your inner creator has something else to say. But preferably I'd have it as a painting...

Here are some keywords: Deep, Progressive, Lucid Dreaming, Ocean, Bedroom...

Please listen to the 3:30 demo of the album to get a better idea.

Thanks,

RoJa

Update:

I've uploaded a few images to kinda help you with the mood/colour tone and direction of what I want, Also, the script writing (I've uploaded a few examples), do it in white colour (left to right, going little bit upwards), preferably on the bottom of the image, simple, one touch, thin hand writing. Have it fading in size (bigger to smaller) as you get to the end of each word. Just like when you sign something, but have it written in two lines.

The whole image should be deep in colour with sort of a glow effect.

Must have
• Name of the album with Script writing,
Should not have
• No paper mosaic art. Image pieced together with cut outs from different sources.

```html
<!DOCTYPE html>
<html lang="en">
<head>
<meta charset="utf-8">
<title>Attic Rivers – Album Cover</title>
<link rel="stylesheet" href="https://fonts.googleapis.com/css2?family=Pinyon+Script&display=swap">
<style>
  :root {
    --glow-white: #fbf8ea;
    --glow-yellow: #f1ec9c;
    --haze-pink: #e6b9d6;
    --dusk-lilac: #c9a3cf;
    --ridge-violet: #4a3a8a;
    --deep-plum: #3b1f3d;
    --ember-orange: #b06a3a;
    --moss-olive: #5a5a2a;
    --title-ink: #f2e6ee;
  }
  * { margin: 0; padding: 0; box-sizing: border-box; }
  html, body {
    width: 1200px;
    height: 1200px;
    overflow: hidden;
    background: var(--deep-plum);
  }
  .album-cover {
    position: relative;
    width: 1200px;
    height: 1200px;
    overflow: hidden;
  }
  .cover-painting {
    position: absolute;
    inset: 0;
    background:
      radial-gradient(ellipse 55% 50% at 22% 22%, var(--glow-white) 0%, rgba(251,248,234,0.85) 30%, rgba(241,236,156,0.6) 55%, rgba(241,236,156,0) 80%),
      radial-gradient(ellipse 45% 25% at 88% 70%, rgba(74,58,138,0.9) 0%, rgba(74,58,138,0) 80%),
      radial-gradient(ellipse 50% 30% at 20% 95%, rgba(59,31,61,0.95) 0%, rgba(59,31,61,0) 85%),
      radial-gradient(ellipse 40% 20% at 60% 98%, rgba(176,106,58,0.7) 0%, rgba(176,106,58,0) 85%),
      radial-gradient(ellipse 35% 25% at 90% 95%, rgba(90,90,42,0.8) 0%, rgba(90,90,42,0) 85%),
      linear-gradient(160deg, var(--glow-yellow) 0%, var(--haze-pink) 45%, var(--dusk-lilac) 58%, var(--deep-plum) 85%);
  }
  .album-title {
    position: absolute;
    left: 575px;
    top: 850px;
    font-family: "Pinyon Script", cursive;
    font-weight: 400;
    color: var(--title-ink);
    line-height: 0.95;
    transform: rotate(-8deg);
    transform-origin: left top;
  }
  .album-title .title-line {
    display: block;
    white-space: nowrap;
  }
  .album-title .title-line--first {
    font-size: 170px;
  }
  .album-title .title-line--second {
    font-size: 150px;
    padding-left: 120px;
  }
</style>
</head>
<body>
  <main class="album-cover">
    <div class="cover-painting" role="img" aria-label="Painted dreamlike seascape: a blazing sun glow in the upper left over a pink haze, violet cliffs with a small distant figure on the right, and dark plum and amber waves along the bottom"></div>
    <h1 class="album-title">
      <span class="title-line title-line--first">Attic</span>
      <span class="title-line title-line--second">Rivers</span>
    </h1>
  </main>
</body>
</html>
```